Modern Informational OBGYN website

Looking for a modern Wordpress website for a general OBGYN practice in Florida with a specialty in High Risk Obstetrics. We had an old Joomla website that crashed and we lost most of the files. It was over 10 years old and needed a refresh anyway.

Our practice serves a multicultural patient population (white, black, Spanish and Indian) and we would like our website to reflect that diversity. Our company colors are sunshine yellow (#ECBF6D) often combined with black, white and steel blue (#7191BE) in the "life" part of our logo (attached) depending on the background. Our tagline is "We're specialist in You!" Overall the site should have a clean modern yet comfortable feel. One that portrays friendliness and competence. At least 6 pages (Home, Obstetrics, Gynecology, News, Patient Education and Resources). Rotating stock pictures or videos are fine for the headers of the pages if the design you're considering calls for it. Interesting and creative use of typography and icons are encouraged.

The home page should have a call to action to schedule an appointment as well as a link to our patient portal. Other than the home and news pages, the other pages should have a similar look and feel. The home page should have sections on "About Us", "Medical Staff" (with pictures and brief bio for 2 male doctors, 2 female midwives and 1 female nurse practitioner), "Services" and "Location". The news page will be a closed blog that will not allow comments or responses. Both the obstetrics and the gynecology pages will have an educational blurb on the respective topics followed by a list of our services for each topic. Would be nice on the obstetrics page to have information and graphics changes that occur during each trimester (but not necessary). The resource page will have sections on at least "Office Forms", Office Policies", "OB Guide" each with multiple downloadable PDF's. Also a section on "Insurance" with a list of all the major insurance plans that we take with links to their company websites. The address, link and map to our hospital and their website can also go on this page. The Patient Education Page can be broken into 3 sections Obstetrics, Gynecology which both will have definition of medical disorders followed by FAQ's and "Helpful Links" which would have links to other website for medical information.

That's all that I can think of right now. The above is to help guide you but I am flexible, if the website design dictates a better flow of information. Looking forward to seeing what you can come up with. Down the road, I will be looking to the winning designer to produce matching brochures, full, half and quarter page media ads to have on hand for the practices further needs.

Target Market(s)

Women looking medical services

Industry/Entity Type

Medical

Coding

Coded - Design and coding required

Number of Pages Required

5+ page

Font styles to use
Sans Serif
Script

Colors

Designer to choose colors to be used in the design.

Requirements
Must have
• None. See projects description for suggestions
Nice to have
• infographics like information on stages of pregnancy on the obstetrics page

```html
<!DOCTYPE html>
<html lang="en">
<head>
<meta charset="utf-8">
<title>Brightday OB/GYN</title>
<link href="https://fonts.googleapis.com/css2?family=Montserrat:wght@400;500;600;700&display=swap" rel="stylesheet">
<style>
:root{
  --navy:#2b3650;
  --ink:#1f2433;
  --text:#4a4f5c;
  --steel:#7191be;
  --steel-btn:#7d97c6;
  --gold:#ecbf6d;
  --gold-deep:#d9a431;
  --white:#ffffff;
}
*{margin:0;padding:0;box-sizing:border-box}
html,body{width:1200px;height:2684px;overflow:hidden}
body{position:relative;font-family:'Montserrat',sans-serif;color:var(--text);background:var(--white)}
.abs{position:absolute}
a{color:inherit;text-decoration:none}

/* hero */
.hero-bg{left:0;top:0;width:1200px;height:640px}
.brand{left:165px;top:34px;font-weight:700;font-size:20px;color:var(--navy);letter-spacing:1px}
.brand small{display:block;font-size:7px;letter-spacing:3px;font-weight:600;margin-top:2px}
.nav{top:40px;left:0;width:1200px;font-size:10px;font-weight:500;color:var(--ink)}
.nav a{position:absolute;top:0}
.eyebrow{left:157px;top:182px;font-size:15px;font-weight:500;letter-spacing:2px;color:var(--navy)}
.headline{left:158px;top:210px;font-size:52px;line-height:57px;font-weight:700;color:var(--navy)}
.btn{display:flex;align-items:center;justify-content:center;background:var(--steel-btn);color:var(--white);font-size:10.5px;font-weight:700;letter-spacing:.6px;box-shadow:0 4px 10px rgba(113,145,190,.3)}
.ghost-word{left:205px;top:360px;font-size:140px;line-height:130px;font-weight:500;letter-spacing:14px;color:rgba(160,170,190,.12);white-space:nowrap;width:480px;overflow:hidden}
.hero-photo{left:677px;top:62px;width:375px;height:492px;border-radius:180px 180px 20px 20px;background:linear-gradient(170deg,#d9b9a4 0%,#efe5da 45%,#f5f1ec 100%)}
.hero-seal{left:540px;top:528px;width:120px;height:120px;border-radius:50%;background:radial-gradient(circle,#fbf1dc 0%,#f6e6c4 60%,#f2dcb0 100%)}

/* section headings */
.kicker{font-size:11px;font-weight:700;letter-spacing:4px}
.h2{font-size:32px;font-weight:500;color:var(--ink)}

/* about */
.about-lead{left:204px;top:826px;font-size:16.5px;font-weight:600;color:var(--ink)}
.about-copy{left:204px;top:861px;width:370px;font-size:14.5px;line-height:25px}
.about-copy p+p{margin-top:12px}
.about-photo{left:678px;top:748px;width:368px;height:368px;border-radius:50%;background:linear-gradient(135deg,#f2ede8 0%,#bfe3ea 50%,#e9ecef 100%)}
.about-glow{left:960px;top:770px;width:150px;height:150px;border-radius:50%;background:rgba(236,191,109,.14)}

/* staff */
.staff-band{left:0;top:1172px;width:1200px;height:704px;background:linear-gradient(120deg,#e7f1f3 0%,#f1f1ef 45%,#f3e6e1 75%,#e6e1ee 100%)}
.staff-photo{width:293px;height:300px}
.staff-card{width:269px;height:188px;background:var(--white);padding:20px 26px;box-shadow:0 8px 24px rgba(60,70,100,.08)}
.staff-card::after{content:"";position:absolute;left:0;bottom:0;width:100%;height:5px;background:linear-gradient(90deg,var(--steel),var(--gold))}
.staff-card h3{font-size:19px;font-weight:600;color:var(--ink);margin-bottom:10px}
.staff-card p{font-size:11px;line-height:20.5px}
.swipe{left:1127px;top:1432px;background:#3c4a5a;color:var(--white);font-size:7.5px;font-weight:600;letter-spacing:.6px;padding:3px 7px;border-radius:8px}
.swipe-dot{left:1135px;top:1451px;width:38px;height:38px;border-radius:50%;background:#3c4a5a}

/* services */
.arrow-btn{width:21px;height:21px;background:var(--steel-btn);display:flex;align-items:center;justify-content:center}
.svc{width:201px;height:225px;border:1px solid #e8e8ec;background:var(--white);padding:0 17px}
.svc-icon{position:absolute;left:17px;top:32px;width:34px;height:34px;border-radius:50%;background:linear-gradient(135deg,#c8d6ea,#f3dfb3)}
.svc-rule{position:absolute;left:17px;top:82px;width:24px;height:2px;background:var(--gold)}
.svc h4{position:absolute;left:17px;top:100px;font-size:13.5px;font-weight:600;color:var(--ink)}
.svc p{position:absolute;left:17px;top:130px;width:170px;font-size:10px;line-height:18px}
.svc .more{position:absolute;left:17px;top:195px;font-size:9px;font-weight:700;color:var(--steel);display:flex;align-items:center;gap:8px}

/* footer */
.map{left:165px;top:2466px;width:285px;height:187px;background:linear-gradient(135deg,#eef0f2 0%,#e3e7ea 60%,#f3e9c8 100%)}
.foot-h{font-size:13px;font-weight:600;color:var(--white);letter-spacing:.3px}
.foot-row{font-size:10.5px;color:var(--white)}
.foot-row b{display:inline-block;width:28px;font-size:8.5px;font-weight:600}
.foot-links a{display:block;font-size:10.5px;color:var(--white);height:20.3px}
</style>
</head>
<body>

<!-- HERO -->
<svg class="abs hero-bg" viewBox="0 0 1200 640" aria-hidden="true">
  <defs>
    <linearGradient id="heroFill" x1="0" y1="0" x2="1" y2="1">
      <stop offset="0" stop-color="#fbf4ea"/>
      <stop offset=".3" stop-color="#fbf7f1"/>
      <stop offset=".6" stop-color="#f1f3f6"/>
      <stop offset="1" stop-color="#ebe4ef"/>
    </linearGradient>
    <radialGradient id="peach" cx=".2" cy=".05" r=".25">
      <stop offset="0" stop-color="#f8d9cc"/>
      <stop offset="1" stop-color="#f8d9cc" stop-opacity="0"/>
    </radialGradient>
  </defs>
  <rect width="1200" height="640" fill="url(#heroFill)"/>
  <rect width="1200" height="640" fill="url(#peach)"/>
  <path d="M0 520 C150 590 330 620 520 612 C720 604 900 545 1020 555 C1110 562 1170 590 1200 605 L1200 640 L0 640 Z" fill="#fff"/>
  <path d="M676 586 C780 560 880 545 960 548 C1060 552 1140 578 1200 612" fill="none" stroke="#ecbf6d" stroke-width="4"/>
</svg>

<div class="abs ghost-word">BRIGHT</div>
<div class="abs hero-photo" role="img" aria-label="Photo of a smiling pregnant woman in a cream cardigan holding her belly"></div>

<div class="abs brand">BRIGHTDAY<small>OB/GYN SERVICES</small></div>
<nav class="abs nav">
  <a style="left:710px">HOME</a>
  <a style="left:771px">ABOUT</a>
  <a style="left:834px">SERVICES</a>
  <a style="left:910px">OUR STAFF</a>
  <a style="left:995px">CONTACT</a>
</nav>

<div class="abs eyebrow">BRIGHTDAY is here for you.</div>
<h1 class="abs headline">We’re Specialist<br>in You!</h1>
<a class="abs btn" style="left:156px;top:353px;width:200px;height:40px">SCHEDULE AN APPOINMENT</a>
<a class="abs btn" style="left:369px;top:353px;width:175px;height:40px">OUR PATIENT PORTAL</a>

<div class="abs hero-seal" role="img" aria-label="Decorative circular seal"></div>

<!-- ABOUT -->
<div class="abs kicker" style="left:0;width:1200px;text-align:center;top:699px;color:var(--gold-deep)">BRIGHTDAY</div>
<h2 class="abs h2" style="left:0;width:1200px;text-align:center;top:722px">About US</h2>

<div class="abs about-lead">Lorem ipsum dolor sit amet, consectetuer</div>
<div class="abs about-copy">
  <p>Adipiscing elit, sed diam nonummy nibh euismod tincidunt ut laoreet dolore magna aliquam erat volutpat. Ut wisi enim ad minim veniam.</p>
  <p>Adipiscing elit, sed diam nonummy nibh euismod tincidunt ut laoreet dolore magna aliquam erat volutpat. Ut wisi enim ad minim veniam.</p>
</div>
<a class="abs btn" style="left:201px;top:1051px;width:125px;height:39px">READ MORE</a>

<div class="abs about-glow" aria-hidden="true"></div>
<div class="abs about-photo" role="img" aria-label="Photo of a doctor in a white coat holding hands with a pregnant patient in a blue gown"></div>

<!-- STAFF -->
<div class="abs staff-band" aria-hidden="true"></div>
<div class="abs kicker" style="left:164px;top:1247px;color:var(--steel)">BRIGHTDAY STAFF</div>
<h2 class="abs h2" style="left:164px;top:1270px">Medical Team</h2>
<a class="abs btn" style="left:937px;top:1255px;width:107px;height:40px">VIEW ALL</a>

<div class="abs staff-photo" style="left:157px;top:1344px;background:linear-gradient(180deg,#dfe3e8,#c9ced6)" role="img" aria-label="Portrait of a senior male doctor in a white coat with a stethoscope"></div>
<div class="abs staff-photo" style="left:482px;top:1344px;background:linear-gradient(180deg,#cfc9cc,#b7b2b6)" role="img" aria-label="Portrait of a bearded male doctor in a white coat"></div>
<div class="abs staff-photo" style="left:801px;top:1344px;background:linear-gradient(180deg,#3fa6c4,#57b5cf)" role="img" aria-label="Portrait of a female doctor in a white coat with a stethoscope"></div>
<div class="abs staff-photo" style="left:1120px;top:1344px;width:80px;background:linear-gradient(180deg,#4c8fa8,#5f9db3)" role="img" aria-label="Portrait of a female nurse practitioner"></div>

<div class="abs staff-card" style="left:172px;top:1625px">
  <h3>Mara Ellison</h3>
  <p>Lorem ipsum dolor sit amet, consectetuer adipiscing elit, sed diam nonummy nibh euismod tincidunt ut laoreet dolore magna aliquam erat volutpat.</p>
</div>
<div class="abs staff-card" style="left:498px;top:1625px">
  <h3>Owen Castell</h3>
  <p style="font-size:10px;line-height:18px">Ut wisi enim ad minim veniam, quis nostrud exerci tation ullamcorper suscipit lobortis nisl ut aliquip ex ea commodo consequat.</p>
</div>
<div class="abs staff-card" style="left:817px;top:1625px">
  <h3>Priya Lanford</h3>
  <p>Lorem ipsum dolor sit amet, consectetuer adipiscing elit, sed diam nonummy nibh euismod tincidunt ut laoreet dolore magna aliquam erat volutpat.</p>
</div>
<div class="abs staff-card" style="left:1136px;top:1625px;width:64px;padding-right:0;overflow:hidden">
  <h3>Rosa</h3>
  <p style="font-size:10px;line-height:18px;white-space:nowrap">Ut wisi<br>nostrud<br>suscipi<br>comm</p>
</div>

<div class="abs swipe">SWIPE LEFT</div>
<div class="abs swipe-dot" aria-hidden="true">
  <svg width="38" height="38" viewBox="0 0 38 38"><path d="M13 14 h12 M13 14 l4 -3 M13 14 l4 3" stroke="#fff" stroke-width="1.6" fill="none" stroke-linecap="round"/><path d="M17 28 v-8 a2 2 0 0 1 4 0 v5 M21 23 a2 2 0 0 1 4 0 v4" stroke="#fff" stroke-width="1.4" fill="none" stroke-linecap="round"/></svg>
</div>

<!-- SERVICES -->
<div class="abs kicker" style="left:160px;top:1964px;color:var(--steel)">BRIGHTDAY SERVICES</div>
<h2 class="abs h2" style="left:158px;top:1991px">Medical Services</h2>
<div class="abs arrow-btn" style="left:997px;top:2004px"><svg width="8" height="10" viewBox="0 0 8 10"><path d="M6 1 L2 5 L6 9" stroke="#fff" stroke-width="1.6" fill="none"/></svg></div>
<div class="abs arrow-btn" style="left:1022px;top:2004px"><svg width="8" height="10" viewBox="0 0 8 10"><path d="M2 1 L6 5 L2 9" stroke="#fff" stroke-width="1.6" fill="none"/></svg></div>

<div class="abs svc" style="left:156px;top:2051px">
  <div class="svc-icon" role="img" aria-label="Gynaecology icon"></div><div class="svc-rule"></div>
  <h4>Gynaecology</h4>
  <p>Lorem ipsum dolor sit amet, consectetuer adipiscing elit, Lorem ipsum dolor....</p>
  <a class="more">LEARN MORE <svg width="36" height="8" viewBox="0 0 36 8"><path d="M0 4 H34 M30 1 L34 4 L30 7" stroke="#b8c0cc" fill="none"/></svg></a>
</div>
<div class="abs svc" style="left:385px;top:2051px">
  <div class="svc-icon" role="img" aria-label="Obstetrical care icon"></div><div class="svc-rule"></div>
  <h4>Obstetrical Care</h4>
  <p>Lorem ipsum dolor sit amet, consectetuer adipiscing elit, Lorem ipsum dolor....</p>
  <a class="more">LEARN MORE <svg width="36" height="8" viewBox="0 0 36 8"><path d="M0 4 H34 M30 1 L34 4 L30 7" stroke="#b8c0cc" fill="none"/></svg></a>
</div>
<div class="abs svc" style="left:614px;top:2051px">
  <div class="svc-icon" role="img" aria-label="Antenatal care icon"></div><div class="svc-rule"></div>
  <h4>Antenatal Care</h4>
  <p>Lorem ipsum dolor sit amet, consectetuer adipiscing elit, Lorem ipsum dolor....</p>
  <a class="more">LEARN MORE <svg width="36" height="8" viewBox="0 0 36 8"><path d="M0 4 H34 M30 1 L34 4 L30 7" stroke="#b8c0cc" fill="none"/></svg></a>
</div>
<div class="abs svc" style="left:842px;top:2051px">
  <div class="svc-icon" role="img" aria-label="Biofeedback icon"></div><div class="svc-rule"></div>
  <h4>Biofeedback</h4>
  <p>Lorem ipsum dolor sit amet, consectetuer adipiscing elit, Lorem ipsum dolor....</p>
  <a class="more">LEARN MORE <svg width="36" height="8" viewBox="0 0 36 8"><path d="M0 4 H34 M30 1 L34 4 L30 7" stroke="#b8c0cc" fill="none"/></svg></a>
</div>

<!-- FOOTER -->
<svg class="abs" style="left:0;top:2290px" width="1200" height="394" viewBox="0 0 1200 394" aria-hidden="true">
  <defs>
    <linearGradient id="footFill" x1="0" y1="0" x2="1" y2="0">
      <stop offset="0" stop-color="#6b7d90"/>
      <stop offset=".6" stop-color="#7c8584"/>
      <stop offset="1" stop-color="#9d9566"/>
    </linearGradient>
  </defs>
  <path d="M0 30 C120 80 300 115 470 112 C700 108 900 35 1060 40 C1130 42 1175 55 1200 65 L1200 394 L0 394 Z" fill="url(#footFill)"/>
  <path d="M0 -5 C120 40 260 85 430 96 C520 101 580 96 630 90" fill="none" stroke="#ecbf6d" stroke-width="4"/>
</svg>

<div class="abs map" role="img" aria-label="Street map showing the clinic location"></div>

<div class="abs foot-h" style="left:504px;top:2475px">CONTACT INFO</div>
<div class="abs foot-row" style="left:507px;top:2512px;line-height:18px"><b>Add.</b>2250 Palm Grove Avenue, Suite<br><span style="margin-left:28px">210, Coral Vale, FL 33099</span></div>
<div class="abs foot-row" style="left:507px;top:2560px"><b>Tel.</b>555-014-2290</div>
<div class="abs foot-row" style="left:507px;top:2585px"><b>Fax</b>555-014-7781</div>
<div class="abs foot-row" style="left:507px;top:2610px"><b>Mail</b>hello@brightdayobgyn.example</div>

<div class="abs foot-h" style="left:746px;top:2475px">QUICK LINKS</div>
<div class="abs foot-links" style="left:746px;top:2513px">
  <a>Home</a><a>About Us</a><a>Services</a><a>Our Staff</a><a>Blog</a><a>Contact</a>
</div>

<div class="abs" style="left:912px;top:2482px;font-size:20px;font-weight:700;color:rgba(255,255,255,.75);letter-spacing:1px">BRIGHTDAY</div>
<div class="abs" style="left:912px;top:2529px;font-size:11px;color:rgba(255,255,255,.85)">© 2022 Brightdayobgyn.</div>

</body>
</html>
```